postcard for Real Estate Agent that sells homes for less than any other agents

My company sells houses for a fraction of what others charge. I have most of the verbiage but I am open to ideas.
Our post card will be 6.25 x 9
We need an image that goes with our words and draws people to take a look
We are playful at the same time very serious about the money we will save our clients. In the past our message has been received as too good to be true. Our old message was "save $6000* when you list with us" We think the "*" was causing people to think their was a catch. Other agents will tell people that we will not do what they will do and that is why they must charge more. We are a full service agency and we will generally do everything that other agents will do and in many cases we will do more than other agents. We are changing this industry and need our message to get to every person that is thinking of selling their home

Target Market(s)

People who want to list their home for sale

Industry/Entity Type

Real Estate Agent

Requirements
Must have
• Image that makes people read the message

```html
<!DOCTYPE html>
<html lang="en">
<head>
<meta charset="utf-8">
<title>Listing Savings Postcard</title>
<link href="https://fonts.googleapis.com/css2?family=Jost:wght@400;500;700&family=Oswald:wght@700&family=Pathway+Gothic+One&display=swap" rel="stylesheet">
<style>
  :root {
    --backdrop: #2a2a2a;
    --ink: #2b2b2b;
    --ink-navy: #23405e;
    --brand-blue: #1b99d6;
    --band-blue: #1a8fcc;
    --frame-green: #6aa84f;
    --logo-green: #5aa33c;
    --panel-top: #cfe9f6;
    --panel-bottom: #ffffff;
    --paper: #ffffff;
  }
  * { box-sizing: border-box; margin: 0; padding: 0; }
  html, body { width: 900px; height: 1200px; overflow: hidden; }
  body { background: var(--backdrop); position: relative; font-family: "Jost", sans-serif; color: var(--ink); }

  /* Front */
  .card-front { position: absolute; left: 45px; top: 30px; width: 810px; height: 562px; overflow: hidden; }
  .house-photo {
    position: absolute; inset: 0;
    background: linear-gradient(180deg, #cfdde6 0%, #e6e2d6 28%, #d8d2c2 55%, #b9c0a8 72%, #6f9a44 84%, #5e8a36 100%);
  }
  .message-panel {
    position: absolute; left: 32px; top: 32px; width: 749px; height: 500px;
    border: 5px solid var(--frame-green);
    background: rgba(255,255,255,0.86);
    text-align: center;
  }
  .lead-in { font-weight: 700; font-size: 42px; margin-top: 36px; line-height: 1; }
  .headline { font-family: "Oswald", sans-serif; font-weight: 700; font-size: 74px; color: var(--brand-blue); line-height: 1; margin-top: 14px; letter-spacing: -0.5px; }
  .statement { font-weight: 700; font-size: 37px; line-height: 1.22; margin-top: 18px; }
  .pitch { font-weight: 700; font-size: 39px; color: var(--brand-blue); line-height: 1.5; margin-top: 6px; }
  .ideas-row {
    display: flex; justify-content: center; align-items: center; gap: 22px;
    font-family: "Pathway Gothic One", sans-serif; font-size: 40px; color: var(--ink-navy); margin-top: 10px;
  }
  .ideas-row .divider { width: 1px; height: 30px; background: var(--frame-green); }

  /* Back */
  .card-back { position: absolute; left: 45px; top: 617px; width: 810px; height: 561px; background: var(--paper); }
  .info-panel { position: absolute; left: 0; top: 0; width: 477px; height: 100%; background: linear-gradient(180deg, var(--panel-top) 0%, #e9f5fb 55%, var(--panel-bottom) 100%); }
  .savings-list { list-style: none; position: absolute; left: 40px; top: 33px; }
  .savings-list li { display: flex; align-items: center; gap: 10px; font-size: 23px; height: 32.5px; }
  .savings-list svg { width: 19px; height: 19px; flex: none; }
  .promise-band {
    position: absolute; left: 0; top: 278px; width: 465px; height: 100px;
    background: var(--band-blue); color: #fff; font-size: 30px; line-height: 1.37;
    padding: 14px 0 0 38px; box-shadow: 6px 8px 8px rgba(0,0,0,0.25);
  }
  .contact { position: absolute; left: 42px; top: 402px; }
  .contact .names { font-size: 26px; margin-bottom: 6px; }
  .contact p { display: flex; align-items: center; gap: 12px; font-size: 27px; height: 40px; font-weight: 500; }
  .contact svg { width: 24px; height: 24px; }
  .stamp-box { position: absolute; left: 690px; top: 29px; width: 89px; height: 99px; border: 1px solid #555; }
  .agency-mark { position: absolute; left: 600px; top: 440px; width: 180px; text-align: center; }
  .agency-name { display: flex; align-items: center; justify-content: center; gap: 8px; font-weight: 700; font-size: 22px; color: var(--ink-navy); }
  .agency-name span.square { width: 16px; height: 16px; background: var(--ink-navy); }
  .agency-phone { font-weight: 500; font-size: 17px; color: var(--logo-green); margin-top: 14px; }
</style>
</head>
<body>
  <section class="card-front">
    <div class="house-photo" role="img" aria-label="Photo of a large suburban house with a green front lawn"></div>
    <div class="message-panel">
      <p class="lead-in">You’d have to be</p>
      <p class="headline">Bat $#@T CRAZY</p>
      <p class="statement">to give an agent $6000.00<br>To put a sign in your yard.</p>
      <p class="pitch">Look at what you can do<br>with $6000.00</p>
      <div class="ideas-row">
        <span>Give it to your Kids</span><span class="divider"></span>
        <span>Build a fence</span><span class="divider"></span>
        <span>Build a deck</span>
      </div>
    </div>
  </section>

  <section class="card-back">
    <div class="info-panel">
      <ul class="savings-list">
        <li><svg viewBox="0 0 20 20"><circle cx="10" cy="10" r="8.5" fill="none" stroke="#1a8fcc" stroke-width="1.5"/><path d="M6 10.5l3 3 5-6" fill="none" stroke="#1a8fcc" stroke-width="1.6"/></svg>Landscape</li>
        <li><svg viewBox="0 0 20 20"><circle cx="10" cy="10" r="8.5" fill="none" stroke="#1a8fcc" stroke-width="1.5"/><path d="M6 10.5l3 3 5-6" fill="none" stroke="#1a8fcc" stroke-width="1.6"/></svg>Take a Vacation</li>
        <li><svg viewBox="0 0 20 20"><circle cx="10" cy="10" r="8.5" fill="none" stroke="#1a8fcc" stroke-width="1.5"/><path d="M6 10.5l3 3 5-6" fill="none" stroke="#1a8fcc" stroke-width="1.6"/></svg>Buy new clothes</li>
        <li><svg viewBox="0 0 20 20"><circle cx="10" cy="10" r="8.5" fill="none" stroke="#1a8fcc" stroke-width="1.5"/><path d="M6 10.5l3 3 5-6" fill="none" stroke="#1a8fcc" stroke-width="1.6"/></svg>Pay off your car</li>
        <li><svg viewBox="0 0 20 20"><circle cx="10" cy="10" r="8.5" fill="none" stroke="#1a8fcc" stroke-width="1.5"/><path d="M6 10.5l3 3 5-6" fill="none" stroke="#1a8fcc" stroke-width="1.6"/></svg>Pay off student loan</li>
        <li><svg viewBox="0 0 20 20"><circle cx="10" cy="10" r="8.5" fill="none" stroke="#1a8fcc" stroke-width="1.5"/><path d="M6 10.5l3 3 5-6" fill="none" stroke="#1a8fcc" stroke-width="1.6"/></svg>Buy New Carpet</li>
        <li><svg viewBox="0 0 20 20"><circle cx="10" cy="10" r="8.5" fill="none" stroke="#1a8fcc" stroke-width="1.5"/><path d="M6 10.5l3 3 5-6" fill="none" stroke="#1a8fcc" stroke-width="1.6"/></svg>Upgrade Appliances</li>
      </ul>
      <div class="promise-band">Full Service Agency at a<br>Fraction of the Cost</div>
      <div class="contact">
        <p class="names">Call Dale or Marcus</p>
        <p><svg viewBox="0 0 24 24"><circle cx="12" cy="12" r="10.5" fill="none" stroke="#1a8fcc" stroke-width="2"/><path d="M8.5 7c-.8.6-1 1.6-.6 2.8 1 2.6 3.3 4.9 5.9 5.9 1.2.4 2.2.2 2.8-.6l-2-1.8-1.3.8c-1.3-.6-2.4-1.7-3-3l.8-1.3z" fill="#1a8fcc"/></svg>555.204.7731</p>
        <p><svg viewBox="0 0 24 24" fill="none" stroke="#1a8fcc" stroke-width="1.8"><circle cx="12" cy="12" r="10"/><ellipse cx="12" cy="12" rx="4.5" ry="10"/><path d="M2 12h20M4 7h16M4 17h16"/></svg>www.HomeSaveRealty.com</p>
      </div>
    </div>
    <div class="stamp-box"></div>
    <div class="agency-mark">
      <div class="agency-name"><span class="square"></span>Keystone Realty</div>
      <div class="agency-phone">555-318-0422</div>
    </div>
  </section>
</body>
</html>
```